Consulting company needs Business Cards - rough concept provided

I'm looking for someone to take our business card idea and make is slick and polished - to communicate our high-end, sophisticated, serious consulting business. We have a rough layout we did in-house. We are open to ideas on repo-ing elements, adjusting sizes, typefaces etc... within the general concept we've already come up with. We want it to be super-clean and sophisticated. We want to keep the white backgrounds, and blue brand colors. Our goal is to print with painted blue edges on thick cardstock. Thank you!!

```html
<!DOCTYPE html>
<html lang="en">
<head>
<meta charset="utf-8">
<title>Tallfern Business Card</title>
<link rel="stylesheet" href="https://fonts.googleapis.com/css2?family=Poppins:wght@400;600;700&family=Open+Sans:wght@700&display=swap">
<style>
  :root {
    --backdrop: #4a4a4a;
    --paper: #f6f6f4;
    --brand-blue: #009fe0;
    --brand-blue-deep: #0a8fcc;
    --ink: #2a2a2a;
    --band-grey: #a3a3a3;
    --ghost: rgba(0, 0, 0, 0.035);
  }
  * { margin: 0; padding: 0; box-sizing: border-box; }
  html, body {
    width: 1093px;
    height: 1200px;
    overflow: hidden;
    background: var(--backdrop);
  }
  .card {
    position: absolute;
    left: 265px;
    border-radius: 24px;
    overflow: hidden;
  }
  .card-front {
    top: 226px;
    width: 576px;
    height: 356px;
    background: var(--paper);
  }
  .card-back {
    top: 621px;
    width: 581px;
    height: 356px;
    background: var(--brand-blue);
  }
  .ghost-name {
    position: absolute;
    left: -20px;
    top: 150px;
    font-family: "Open Sans", sans-serif;
    font-weight: 700;
    font-size: 76px;
    letter-spacing: 1px;
    color: var(--ghost);
    transform: rotate(-37deg);
    transform-origin: left top;
    white-space: nowrap;
  }
  .name-marker {
    position: absolute;
    left: 0;
    top: 43px;
    width: 17px;
    height: 30px;
    background: var(--brand-blue);
  }
  .person {
    position: absolute;
    left: 26px;
    top: 37px;
    font-family: "Poppins", sans-serif;
  }
  .person-name {
    font-weight: 700;
    font-size: 21px;
    line-height: 24px;
    color: var(--brand-blue);
    letter-spacing: -0.3px;
  }
  .person-role {
    font-weight: 400;
    font-size: 16.5px;
    line-height: 18px;
    color: var(--ink);
  }
  .wordmark {
    position: absolute;
    right: 20px;
    top: 38px;
    font-family: "Open Sans", sans-serif;
    font-weight: 700;
    font-size: 40px;
    line-height: 44px;
    color: var(--brand-blue);
    letter-spacing: -0.5px;
  }
  .contacts {
    position: absolute;
    left: 26px;
    top: 282px;
    font-family: "Poppins", sans-serif;
    font-size: 17.5px;
    line-height: 21px;
    color: var(--ink);
    list-style: none;
  }
  .contacts li { display: flex; align-items: center; gap: 7px; }
  .contacts svg { width: 16px; height: 16px; flex: none; }
  .address {
    position: absolute;
    right: 25px;
    top: 280px;
    font-family: "Poppins", sans-serif;
    font-style: normal;
    font-size: 17.5px;
    line-height: 21px;
    color: var(--ink);
    text-align: right;
  }
  .edge-band {
    position: absolute;
    left: 0;
    bottom: 0;
    width: 576px;
    height: 14px;
  }
  .back-wordmark {
    position: absolute;
    left: 0;
    right: 0;
    top: 136px;
    text-align: center;
    font-family: "Open Sans", sans-serif;
    font-weight: 700;
    font-size: 66px;
    line-height: 80px;
    color: var(--brand-blue-deep);
    letter-spacing: -0.5px;
  }
</style>
</head>
<body>
  <section class="card card-front">
    <div class="ghost-name" aria-hidden="true">TALLFERN</div>
    <div class="name-marker"></div>
    <div class="person">
      <p class="person-name">DANA HOLLOWAY</p>
      <p class="person-role">Brand Consultant</p>
    </div>
    <div class="wordmark">TALLFERN</div>
    <ul class="contacts">
      <li>
        <svg viewBox="0 0 16 16" aria-hidden="true"><path d="M4 1.5l2.3 3-1.4 1.6c.8 1.8 2.2 3.2 4 4l1.6-1.4 3 2.3-1.2 2.5c-5.6-.4-10-4.8-10.3-10.4z" fill="none" stroke="#009fe0" stroke-width="1.6" stroke-linejoin="round"/></svg>
        <span>(555) 014 2290</span>
      </li>
      <li>
        <svg viewBox="0 0 16 16" aria-hidden="true"><rect x="0.5" y="3" width="15" height="10" fill="#009fe0"/><path d="M0.5 3l7.5 6 7.5-6M0.5 13l5.5-5M15.5 13l-5.5-5" fill="none" stroke="#f6f6f4" stroke-width="1"/></svg>
        <span>dana@tallfern.com</span>
      </li>
    </ul>
    <address class="address">4820 Harbor Row<br>Ste 210 Lakeview, CA 90010</address>
    <svg class="edge-band" viewBox="0 0 576 14" aria-hidden="true">
      <polygon points="0,0 288,0 283,14 0,14" fill="var(--band-grey)"/>
      <polygon points="294,0 576,0 576,14 289,14" fill="var(--brand-blue)"/>
    </svg>
  </section>

  <section class="card card-back">
    <div class="back-wordmark">TALLFERN</div>
  </section>
</body>
</html>
```